来年3月31日に期限が迫っているインボイス制度について、まだまだ関係ある方にも周知はされていません。
もちろん税務関係なので、税理士さんを始めとして、いろいろな方が、セミナー開催やポルネットとかでも語っていらっしゃいます。
ところが、職種によっては、今更、込み入った話など聞きたくない、面倒だ、聞いてもよく理解できないといった方が多々おられます。
私は、建築関係の経理に携わっており、身近にも、そんな方々を目にしていて危惧している状態です。
これが全国となったら、いったいどれだけの人が、わからないまま期日を迎えてしまうのでしょう。
その中で、とくに今回 ひとり親方にターゲットを絞って、せめて、その方々に向けて、いちからわかるように、しかも語りかけるつもりで書きました。
本文を添付いたしますので、その意向を汲んでいただいた上での電子書籍の表紙デザインをお願いしたいです。
一目で見て、これなら一度読んでみるかと思っていただけるようなものを期待しております。
是非とも、宜しくお願い致します。

```html
<!DOCTYPE html>
<html lang="ja">
<head>
<meta charset="utf-8">
<title>ひとり親方のための いちからわかるインボイス制度</title>
<link rel="stylesheet" href="https://fonts.googleapis.com/css2?family=Noto+Sans+JP:wght@700;900&display=swap">
<style>
  :root {
    --sun-yellow: #ffd21f;
    --sun-orange: #f7b500;
    --leaf-green: #8cc63f;
    --ink: #1a1a1a;
    --paper: #ffffff;
    --figure-grey: #8b8f96;
    --figure-tone: #b9bcc1;
  }
  html, body {
    margin: 0;
    padding: 0;
    width: 750px;
    height: 1200px;
    overflow: hidden;
    background: var(--paper);
  }
  .cover {
    position: relative;
    width: 750px;
    height: 1200px;
    overflow: hidden;
    font-family: "Noto Sans JP", sans-serif;
    color: var(--ink);
  }
  .cover__top {
    position: absolute;
    inset: 0 0 auto 0;
    height: 590px;
    background: linear-gradient(160deg, var(--sun-yellow), var(--sun-orange));
  }
  .cover__bottom {
    position: absolute;
    left: 0; right: 0; top: 590px; bottom: 0;
    background: var(--leaf-green);
  }
  .worker-figure {
    position: absolute;
    left: 470px;
    top: 470px;
    width: 290px;
    height: 730px;
    border-radius: 140px 140px 0 0;
    background: linear-gradient(180deg, var(--sun-yellow) 0 16%, var(--figure-tone) 16% 38%, var(--figure-grey) 38% 100%);
    opacity: 0.9;
  }
  .audience-bubble {
    position: absolute;
    left: 88px;
    top: 22px;
    width: 574px;
    height: 92px;
  }
  .audience-bubble svg { position: absolute; inset: 0; }
  .audience-bubble__text {
    position: relative;
    margin: 0;
    line-height: 92px;
    text-align: center;
    font-size: 50px;
    font-weight: 900;
    letter-spacing: 2px;
  }
  .lead {
    position: absolute;
    left: 0; right: 0;
    top: 160px;
    margin: 0;
    text-align: center;
    font-size: 62px;
    font-weight: 900;
    letter-spacing: 2px;
  }
  .lead__dot { position: relative; }
  .lead__dot::before {
    content: "";
    position: absolute;
    left: 50%;
    top: 2px;
    width: 9px; height: 9px;
    margin-left: -4.5px;
    border-radius: 50%;
    background: var(--ink);
  }
  .title-plate {
    position: absolute;
    left: 72px;
    top: 280px;
    width: 606px;
    height: 278px;
    border-radius: 28px;
    background: var(--ink);
    color: var(--paper);
    text-align: center;
  }
  .title-plate h1 {
    margin: 0;
    padding-top: 14px;
    font-size: 114px;
    font-weight: 900;
    line-height: 126px;
    letter-spacing: 2px;
  }
  .outlined {
    -webkit-text-stroke: 14px var(--paper);
    paint-order: stroke fill;
    font-weight: 900;
  }
  .question {
    position: absolute;
    left: 24px;
    top: 628px;
    margin: 0;
    line-height: 1;
  }
  .question__line1 { display: block; font-size: 96px; letter-spacing: -2px; }
  .question__line2 { display: block; font-size: 116px; letter-spacing: -4px; }
  .question__line3 { display: block; font-size: 90px; padding-left: 240px; }
  .aside {
    position: absolute;
    left: 30px;
    top: 862px;
    width: 220px;
    margin: 0;
    font-size: 20px;
    line-height: 1.2;
    text-align: center;
    transform: rotate(-10deg);
    -webkit-text-stroke: 7px var(--paper);
    paint-order: stroke fill;
    font-weight: 900;
  }
  .promise {
    position: absolute;
    left: 160px;
    top: 932px;
    margin: 0;
    font-size: 60px;
    line-height: 1.08;
  }
  .promise span { display: block; }
  .author {
    position: absolute;
    left: 225px;
    top: 1128px;
    margin: 0;
    color: var(--paper);
    font-size: 38px;
    font-weight: 900;
    letter-spacing: 2px;
    -webkit-text-stroke: 8px var(--ink);
    paint-order: stroke fill;
  }
  .author small { font-size: 26px; margin-left: 6px; }
</style>
</head>
<body>
<main class="cover">
  <div class="cover__top"></div>
  <div class="cover__bottom"></div>

  <div class="worker-figure" role="img" aria-label="ヘルメットをかぶり作業着を着た建設職人のイラスト"></div>

  <div class="audience-bubble">
    <svg viewBox="0 0 574 120" width="574" height="120" aria-hidden="true">
      <path d="M40 4 H534 Q570 4 570 44 V56 Q570 88 534 88 H300 L280 114 L262 88 H40 Q4 88 4 56 V44 Q4 4 40 4 Z"
            fill="var(--paper)" stroke="var(--ink)" stroke-width="6" stroke-linejoin="round"/>
    </svg>
    <p class="audience-bubble__text">ひとり親方のための</p>
  </div>

  <p class="lead">いちから<span class="lead__dot">わ</span><span class="lead__dot">か</span><span class="lead__dot">る</span></p>

  <div class="title-plate">
    <h1>インボイス<br>制度</h1>
  </div>

  <h2 class="question outlined">
    <span class="question__line1">そもそも</span>
    <span class="question__line2">インボイス</span>
    <span class="question__line3">って何？</span>
  </h2>

  <p class="aside">なんでもかんでも<br>カタカナ使わずに<br>日本語で言ってくれ!</p>

  <p class="promise outlined">
    <span>誰でもわかる</span>
    <span>ように解説</span>
    <span>します!!</span>
  </p>

  <p class="author">森田由美子<small>著</small></p>
</main>
</body>
</html>
```